skyROAMER Helicopter Tour WordPress Website Design

SkyROAMER (skyroamer-example.com) is a premium helicopter tour company offering scenic flights in two Florida cities: Tampa and Sarasota. We are seeking a full Wordpress website redesign that is modern, upbeat, inviting, and highly conversion‑focused. The new site should feel energetic and trustworthy, reflect the excitement of helicopter sightseeing, and maintain our recognizable SkyROAMER color palette—while updating the overall look to feel fresh, clean, and current.
The website must be SEO‑friendly, mobile‑optimized, and easy to navigate. It should highlight our 5‑star customer reviews, showcase our tours clearly, and integrate seamlessly with TripLantern for instant online booking. The design should support a premium aviation experience while remaining friendly and accessible to tourists, families, couples, and adventure seekers.

These elements are essential and must be included in the design:

Brand & UX:
- Modern, upbeat, inviting design
- SEO‑friendly structure and layout
- Easy navigation and clear user flow
- Light grey “SR” background logo watermark (as used on current site)
- Clean, aviation‑inspired typography and layout

Conversion Features:
- Instant booking above the fold (TripLantern integration)
- Live Pindle Ratings carousel
- Tour comparison table (duration, route, price, etc.)
- FAQ expandable section
- Gift Cards page (highlighted as a major offering)
- What to Expect timeline (Arrive → Check‑In → Safety Briefing → Flight → Photos)
- Weather transparency widget (clear messaging about weather‑dependent flights

Content Structure:
- Separate pages for Tampa, Sarasota, and Gender Reveal Flights
- Pilot/Team profiles with short bios
- Highlighted features:
- Doors‑Off option
- Sunset flights
- Romantic packages
- Champagne add‑ons

Colors:
Use the existing SkyROAMER palette as the foundation, but modernize it.
- Background: Clean with the light grey “SR” watermark integrated tastefully.
The overall color direction should feel bright, premium, energetic, and trustworthy

Target Market(s)

Tourists visiting Tampa or Sarasota, Families looking for memorable activities, Couples seeking romantic experiences (sunset flights, proposals, anniversaries), Adventure seekers and content creators, Locals celebrating birthdays, holidays, or special occasions, Gender reveal clients looking for a unique aerial reveal experience

Industry/Entity Type

Travel & Tourism / Aviation / Helicopter Tours / Experience‑based Activities

Requirements
Must have
• These elements are essential and must be included in the design: Brand & UX - Modern, upbeat, inviting design / SEO‑friendly structure and layout / Easy navigation and clear user flow / Light grey “SR” background logo watermark (as used on current site) / Clean, aviation‑inspired typography and layout
Nice to have
• Interactive route map showing flight paths / Subtle motion or parallax effects in hero sections / Animated icons or micro‑interactions / Social media integration (Photavia grid, ClipNest clips) / Sticky mobile booking bar / Video header or short aerial footage loop / Subtle aviation‑themed graphic elements (rotor blur, sky gradients, etc.
Should not have
• No dark, heavy, or overly moody themes / No outdated fonts or overly playful typography / No cluttered layouts or excessive text blocks / No stocky, generic tourism imagery / No slow‑loading animations or heavy effects that hurt SEO

```html
<!DOCTYPE html>
<html lang="en">
<head>
<meta charset="utf-8">
<title>SkyROAMER Helicopter Tours</title>
<link rel="stylesheet" href="https://fonts.googleapis.com/css2?family=Montserrat:wght@400;600;700;800&family=Oswald:wght@600;700&family=Poppins:wght@300;400;500;600&display=swap">
<style>
:root{
  --blue:#0d63e0;
  --blue-deep:#1c5fb4;
  --blue-soft:#78a9dd;
  --band:#e6f0fc;
  --ink:#222a35;
  --muted:#6f7782;
  --line:#dfe5ee;
  --mark:#e3ebf5;
  --foot:#3a3e45;
  --white:#fff;
}
*{box-sizing:border-box;margin:0;padding:0}
html,body{width:1200px;height:5042px;overflow:hidden;background:#fff}
body{font-family:"Poppins",sans-serif;color:var(--ink);position:relative}
.page{position:relative;width:1200px;height:5042px;overflow:hidden}
.abs{position:absolute}
.btn{position:absolute;display:flex;align-items:center;justify-content:center;background:var(--blue);color:#fff;font-family:"Montserrat",sans-serif;font-weight:600;font-size:11px;letter-spacing:.3px;border-radius:3px;text-transform:uppercase}
.h2{position:absolute;left:0;width:1200px;text-align:center;font-family:"Montserrat",sans-serif;font-weight:800;font-size:33px;line-height:37px;color:var(--blue-deep);text-transform:uppercase}
.h2 span{display:block;color:var(--blue-soft)}
.wave{position:absolute;left:570px;width:60px;height:8px}
.mark{position:absolute;font-family:"Montserrat",sans-serif;font-weight:800;color:var(--mark);line-height:1}
.photo{position:absolute;border-radius:10px;overflow:hidden}

/* hero */
.hero{left:0;top:0;width:1200px;height:646px;background:linear-gradient(180deg,#3a4048 0%,#59626c 35%,#8f9aa5 65%,#dfe3e8 88%,#fff 100%)}
.brand{position:absolute;left:92px;top:42px;display:flex;align-items:center;gap:8px;font-family:"Montserrat",sans-serif;font-weight:700;font-size:22px;color:#fff}
.brand i{width:14px;height:14px;border-radius:50%;background:var(--blue);display:block}
.nav{position:absolute;top:38px;left:544px;display:flex;gap:0;font-family:"Montserrat",sans-serif;font-size:10px;font-weight:600;color:#fff;text-transform:uppercase}
.nav a{position:absolute;white-space:nowrap;color:#fff;text-decoration:none}
.hero-title{position:absolute;top:222px;left:0;width:1200px;text-align:center;font-family:"Oswald",sans-serif;font-weight:700;font-size:48px;line-height:50px;color:#fff;text-transform:uppercase}
.hero-sub{position:absolute;top:326px;left:0;width:1200px;text-align:center;font-family:"Oswald",sans-serif;font-weight:600;font-size:13px;color:#fff;text-transform:uppercase}
.side-tab{position:absolute;left:1162px;top:636px;width:38px;height:166px;background:var(--blue);border-radius:8px 0 0 8px;color:#fff;font-family:"Montserrat",sans-serif;font-weight:600;font-size:9.5px;display:flex;align-items:center;justify-content:center}
.side-tab span{transform:rotate(-90deg);white-space:nowrap}

/* memories */
.mem-text{position:absolute;left:613px;top:851px;width:405px;font-size:11px;line-height:17.6px;color:#333}
.mem-h{position:absolute;left:613px;top:744px;font-family:"Montserrat",sans-serif;font-weight:800;font-size:33px;line-height:35px;color:var(--blue-deep)}
.mem-h span{display:block;color:var(--blue-soft)}
.play{position:absolute;left:349px;top:1020px;width:22px;height:16px;background:#e3211c;border-radius:4px}

/* city cards */
.card-label{position:absolute;background:#fff;border-radius:10px 10px 0 0;padding:16px 0 0 0}
.city{position:absolute;font-family:"Montserrat",sans-serif;font-weight:800;font-size:24px;color:var(--blue-deep);text-transform:uppercase}
.state{position:absolute;font-size:16px;color:var(--blue-soft);font-weight:300}
.soon{position:absolute;font-family:"Montserrat",sans-serif;font-size:9px;font-weight:700;color:#e23a2c}

/* reviews */
.band{position:absolute;left:0;width:1200px;background:var(--band)}
.rv-summary{position:absolute;left:192px;top:1870px;width:96px;text-align:center}
.rv-card{position:absolute;top:1840px;width:213px;height:146px;background:#fff;border-radius:6px;padding:12px;font-size:9.5px;line-height:14px;color:#333}
.rv-card .who{display:flex;gap:8px;align-items:center}
.avatar{width:22px;height:22px;border-radius:50%;color:#fff;font-size:10px;font-weight:600;display:flex;align-items:center;justify-content:center}
.rv-card b{display:block;font-size:9.5px;font-weight:600}
.rv-card small{display:block;font-size:8px;color:#a0a6ae}
.stars{color:#f6b400;font-size:12px;letter-spacing:1px;margin:6px 0 5px}
.more{color:#a0a6ae;font-size:8px;margin-top:2px}
.arrow-s{position:absolute;top:1905px;font-size:14px;color:#555}
.verified{position:absolute;left:884px;top:1994px;width:106px;height:17px;border-radius:9px;background:#fff;font-size:8px;display:flex;align-items:center;justify-content:center;gap:4px;color:#333}
.verified i{width:8px;height:8px;border-radius:50%;background:#2aa84a;display:block}

/* tours */
.tour-label{position:absolute;top:2509px;width:317px;height:113px;background:#fff;border-radius:10px 10px 0 0;padding:16px 20px 0 14px}
.tour-label h3{font-family:"Montserrat",sans-serif;font-weight:800;font-size:17px;line-height:21px;color:var(--blue-deep);text-transform:uppercase;width:240px}
.tour-label ul{list-style:none;margin-top:6px;font-size:10px;line-height:15px;color:#444}
.tour-label li::before{content:"› ";color:var(--blue)}
.tour-label li em{font-style:normal;color:var(--blue)}
.cal{position:absolute;right:22px;top:22px;width:26px;height:26px;background:var(--blue);border-radius:4px;display:flex;align-items:center;justify-content:center}
.tour-nav{position:absolute;top:2662px;font-size:18px;color:#333}

/* timeline */
.step{position:absolute;width:172px;height:130px;background:linear-gradient(90deg,#fff 0%,#fff 60%,#eef4fd 100%);box-shadow:0 10px 24px rgba(35,90,160,.12);display:flex;flex-direction:column;align-items:center;justify-content:center;gap:8px;font-family:"Montserrat",sans-serif;font-weight:700;font-size:17px;color:#2f7ac8;text-align:center;line-height:17px}
.step::after{content:"";position:absolute;right:-10px;top:54px;border-left:10px solid #f4f8fe;border-top:10px solid transparent;border-bottom:10px solid transparent}
.step.last::after{display:none}

/* faq */
.faq{position:absolute;left:337px;width:528px;border:1px solid var(--line);border-radius:4px;background:#fff;padding:0 12px;font-family:"Montserrat",sans-serif;font-size:10px;font-weight:700;color:#222}
.faq .q{display:flex;justify-content:space-between;align-items:center;height:32px}
.faq .q.open{color:var(--blue-deep);height:26px}
.faq .a{font-family:"Poppins",sans-serif;font-weight:400;font-size:10px;color:#333}
.tog{width:15px;height:15px;border-radius:50%;background:#d6d9de;display:block}
.tog.on{background:var(--blue)}

/* shorts */
.short{position:absolute;top:3881px;width:186px;height:282px;border-radius:8px}
.short i{position:absolute;right:10px;top:10px;width:16px;height:16px;border:2px solid #fff;border-radius:4px}
.social{position:absolute;top:4194px;width:162px;height:37px;border-radius:3px;display:flex;align-items:center;justify-content:center;gap:8px;font-family:"Montserrat",sans-serif;font-weight:600;font-size:15px;color:#fff}
.social i{width:13px;height:13px;border-radius:50%;border:2px solid #fff;display:block}

/* inquiry */
.field{position:absolute;height:34px;border:1px solid var(--line);border-radius:2px;font-size:9.5px;color:#9aa1aa;padding:10px 12px}

/* weather */
.weather{position:absolute;left:0;top:4736px;width:133px;height:59px;background:#2d3138;color:#fff;border-radius:0 6px 6px 0;padding:6px 8px;font-size:8px}
.weather b{display:block;font-size:18px;font-weight:600;line-height:22px}

/* footer */
.footer{position:absolute;left:0;top:4765px;width:1200px;height:245px;background:linear-gradient(180deg,#44484f,#33363c)}
.foot-brand{position:absolute;left:157px;top:4880px;display:flex;align-items:center;gap:8px;font-family:"Montserrat",sans-serif;font-weight:700;font-size:22px;color:#fff}
.foot-brand i{width:14px;height:14px;border-radius:50%;background:var(--blue);display:block}
.foot-h{position:absolute;font-family:"Montserrat",sans-serif;font-weight:600;font-size:15px;color:#6fa8ea}
.foot-list{position:absolute;font-size:11px;line-height:20px;color:#fff;list-style:none}
.contact{position:absolute;left:382px;font-size:11.5px;line-height:15px;color:#fff;display:flex;gap:8px}
.contact svg{flex:none;margin-top:2px}
.copy{position:absolute;left:0;top:5010px;width:1200px;height:32px;background:var(--blue);color:#fff;font-size:10px;padding:9px 157px}
.sq{position:absolute;top:5020px;width:12px;height:12px;background:#fff;border-radius:2px}
</style>
</head>
<body>
<div class="page">

<!-- HERO -->
<header class="abs hero">
  <div class="photo" role="img" aria-label="Pilot and guests seated in a helicopter cockpit with headsets, sunset light" style="left:0;top:0;width:1200px;height:646px;border-radius:0;background:linear-gradient(160deg,rgba(30,40,55,.55),rgba(120,130,140,.2) 60%,rgba(255,255,255,0) 95%)"></div>
  <div class="brand"><i></i>SkyROAMER</div>
  <nav class="nav">
    <a style="left:0">Sarasota</a>
    <a style="left:84px">Tampa</a>
    <a style="left:147px">Special Events</a>
    <a style="left:262px">Influencer</a>
    <a style="left:356px">Contact Us</a>
  </nav>
  <a class="btn" style="left:1000px;top:29px;width:106px;height:34px">Book Now</a>
  <h1 class="hero-title">The Ultimate<br>Helicopter Experience</h1>
  <p class="hero-sub">Say yes to new adventures.</p>
  <a class="btn" style="left:520px;top:364px;width:171px;height:30px;text-transform:none;font-size:11px">Book Your SkyROAMER</a>
</header>
<a class="side-tab"><span>Book Your SkyROAMER</span></a>

<!-- MEMORIES -->
<section>
  <div class="mark" style="left:830px;top:755px;font-size:56px">SR</div>
  <div class="mark" style="left:900px;top:1050px;font-size:130px">SR</div>
  <div class="photo" role="img" aria-label="Smiling pilot and two passengers wearing headsets inside a helicopter" style="left:227px;top:726px;width:313px;height:231px;background:linear-gradient(135deg,#c8b7a3,#8f98a2 55%,#3d4651)"></div>
  <div class="photo" role="img" aria-label="Guest posing beside a helicopter on the tarmac" style="left:157px;top:885px;width:228px;height:160px;background:linear-gradient(160deg,#b9d3ef,#d7c9b8 55%,#5b5e63);border:4px solid #fff"></div>
  <div class="play"></div>
  <h2 class="mem-h">WE CREATE<span>MEMORIES</span></h2>
  <svg class="wave" style="left:613px;top:818px" viewBox="0 0 60 8"><path d="M0 4 q4 -4 8 0 t8 0 t8 0 t8 0 t8 0 t8 0 t8 0" fill="none" stroke="#1c5fb4" stroke-width="1.6"/></svg>
  <p class="mem-text">SkyROAMER Offers Some Of The Most Exciting Florida Helicopter Tours, Empowering You To Design Your Own Custom Aerial Adventure Across Three Iconic Cities. With Popular Helicopter Tours In Tampa And Sarasota. Whether You Prefer A Smooth, Air-Conditioned Ride Or Crave The Thrill Of A Doors-Off Helicopter Tour, We Deliver Breathtaking Views And Unforgettable Moments From Takeoff To Landing.</p>
  <a class="btn" style="left:613px;top:982px;width:107px;height:32px">Read More</a>
</section>

<!-- CHOOSE -->
<section>
  <div class="mark" style="left:385px;top:1140px;font-size:56px">SR</div>
  <h2 class="h2" style="top:1139px">Choose Your<span>SkyROAMER</span></h2>
  <svg class="wave" style="top:1218px" viewBox="0 0 60 8"><path d="M0 4 q4 -4 8 0 t8 0 t8 0 t8 0 t8 0 t8 0 t8 0" fill="none" stroke="#1c5fb4" stroke-width="1.6"/></svg>

  <div class="photo" role="img" aria-label="Tampa skyline at dusk over the river" style="left:157px;top:1253px;width:430px;height:297px;background:linear-gradient(180deg,#7a87a8,#c69a86 45%,#3a3d4a 75%,#1c2a3c)"></div>
  <div class="card-label" style="left:180px;top:1458px;width:192px;height:112px"></div>
  <div class="city" style="left:197px;top:1478px">Tampa</div>
  <div class="state" style="left:197px;top:1508px">Florida</div>
  <a class="btn" style="left:197px;top:1540px;width:100px;height:28px">Book Now</a>

  <div class="photo" role="img" aria-label="Sarasota waterfront and marina at twilight" style="left:613px;top:1253px;width:430px;height:297px;background:linear-gradient(180deg,#8a92b0,#a9a6b8 40%,#3c4a5c 70%,#25344a)"></div>
  <div class="card-label" style="left:636px;top:1458px;width:192px;height:112px"></div>
  <div class="city" style="left:653px;top:1478px">Sarasota</div>
  <div class="state" style="left:653px;top:1508px">Florida</div>
  <a class="btn" style="left:653px;top:1540px;width:100px;height:28px">Book Now</a>

  <div class="photo" role="img" aria-label="St. Augustine waterfront tower under blue sky" style="left:1069px;top:1253px;width:430px;height:297px;background:linear-gradient(180deg,#8fc0ee,#cfe0ef 55%,#8c94a0)"></div>
  <div class="card-label" style="left:1092px;top:1458px;width:192px;height:112px"></div>
  <div class="soon" style="left:1109px;top:1468px">COMING SOON</div>
  <div class="city" style="left:1109px;top:1478px">St. Augustine</div>
  <div class="state" style="left:1109px;top:1508px">Florida</div>
  <a class="btn" style="left:1109px;top:1540px;width:100px;height:28px">Book Now</a>
</section>

<!-- REVIEWS -->
<section class="band" style="top:1660px;height:430px"></section>
<div class="mark" style="left:770px;top:1735px;font-size:56px;color:#d5e3f4">SR</div>
<h2 class="h2" style="top:1726px">What Customers<span>Are Saying</span></h2>
<svg class="wave" style="top:1804px" viewBox="0 0 60 8"><path d="M0 4 q4 -4 8 0 t8 0 t8 0 t8 0 t8 0 t8 0 t8 0" fill="none" stroke="#1c5fb4" stroke-width="1.6"/></svg>
<div class="rv-summary">
  <div style="font-family:Montserrat,sans-serif;font-weight:700;font-size:14px">EXCELLENT</div>
  <div class="stars" style="font-size:18px;margin:2px 0">★★★★★</div>
  <div style="font-size:8px">Based on <b>225 reviews</b></div>
  <div style="font-family:Poppins,sans-serif;font-weight:600;font-size:18px;color:#4a6ea8;margin-top:2px">Pindle</div>
</div>
<div class="arrow-s" style="left:332px">‹</div>
<div class="rv-card" style="left:339px">
  <div class="who"><span class="avatar" style="background:#5a6fd1">K</span><div><b>Kai Marlow</b><small>2 weeks ago</small></div></div>
  <div class="stars">★★★★★</div>
  Great experience! Dario is a terrific pilot and very friendly!
</div>
<div class="rv-card" style="left:562px">
  <div class="who"><span class="avatar" style="background:#9aa3b0">TJ</span><div><b>TJ Barrows</b><small>3 weeks ago</small></div></div>
  <div class="stars">★★★★★</div>
  Amazing experience. Dario was our pilot and he was awesome. Just great vibes.
</div>
<div class="rv-card" style="left:787px">
  <div class="who"><span class="avatar" style="background:#1f8a6d">N</span><div><b>Nessa Ortega</b><small>2 weeks ago</small></div></div>
  <div class="stars">★★★★★</div>
  Such a great experience! My husband booked us the romantic flight as a surprise and it was absolutely adorable. Definitely need to have a good tour...
  <div class="more">Read more</div>
</div>
<div class="arrow-s" style="left:1000px">›</div>
<div class="verified">Verified by Revuely <i></i></div>

<!-- TOUR COMPARISON -->
<section>
  <div class="mark" style="left:340px;top:2180px;font-size:56px">SR</div>
  <h2 class="h2" style="top:2176px">Tour<span>Comparison Table</span></h2>
  <svg class="wave" style="top:2253px" viewBox="0 0 60 8"><path d="M0 4 q4 -4 8 0 t8 0 t8 0 t8 0 t8 0 t8 0 t8 0" fill="none" stroke="#1c5fb4" stroke-width="1.6"/></svg>

  <div class="photo" role="img" aria-label="Passenger feet above the city from an open helicopter door" style="left:-299px;top:2290px;width:430px;height:297px;background:linear-gradient(180deg,#2c3340,#6b5b4e 50%,#1d2430)"></div>
  <div class="tour-label" style="left:-240px"><span class="cal"></span></div>
  <div class="abs" style="left:0;top:2600px;font-size:10px;color:#444">ches</div>

  <div class="photo" role="img" aria-label="Downtown Sarasota skyline at dusk" style="left:157px;top:2290px;width:430px;height:297px;background:linear-gradient(180deg,#7a87a8,#c69a86 45%,#3a3d4a 75%,#1c2a3c)"></div>
  <div class="tour-label" style="left:215px">
    <h3>The Downtown Tour (Sarasota)</h3>
    <span class="cal"><svg width="12" height="12" viewBox="0 0 12 12"><rect x="1" y="2" width="10" height="9" rx="1" fill="none" stroke="#fff" stroke-width="1.3"/><path d="M1 5h10M4 1v2M8 1v2" stroke="#fff" stroke-width="1.3"/></svg></span>
    <ul><li>Starting At <em>$179</em></li><li><em>20 Minutes</em> Of Flight Time</li><li>See Downtown Sarasota From A Bird's-Eye View</li></ul>
  </div>

  <div class="photo" role="img" aria-label="Pilot flying over the coastline seen from the cockpit" style="left:613px;top:2290px;width:430px;height:297px;background:linear-gradient(180deg,#9cc4e6,#dcd3c3 45%,#5b6b7a)"></div>
  <div class="tour-label" style="left:671px">
    <h3>The Ultimate Beach Tour (Tampa)</h3>
    <span class="cal"><svg width="12" height="12" viewBox="0 0 12 12"><rect x="1" y="2" width="10" height="9" rx="1" fill="none" stroke="#fff" stroke-width="1.3"/><path d="M1 5h10M4 1v2M8 1v2" stroke="#fff" stroke-width="1.3"/></svg></span>
    <ul><li>Starting At <em>$239</em></li><li><em>35 Minutes</em> Of Flight Time</li><li>See Marine Wildlife And Florida's #1 Beaches</li></ul>
  </div>

  <div class="photo" role="img" aria-label="Bay at sunset under a purple sky" style="left:1069px;top:2290px;width:430px;height:297px;background:linear-gradient(180deg,#3a3c55,#a27968 50%,#2a2f3e)"></div>
  <div class="tour-label" style="left:1127px">
    <h3>The D… Tour (Tamp…</h3>
    <ul><li>Starting A…</li><li><em>35 Minut…</em></li><li>See Marin…</li></ul>
  </div>

  <div class="tour-nav" style="left:518px">‹</div>
  <a class="btn" style="left:552px;top:2656px;width:94px;height:30px">View All</a>
  <div class="tour-nav" style="left:670px">›</div>
</section>

<!-- TIMELINE -->
<section class="band" style="top:2763px;height:447px"></section>
<div class="mark" style="left:755px;top:2855px;font-size:56px;color:#d5e3f4">SR</div>
<h2 class="h2" style="top:2848px">What To Expect<span>Timeline</span></h2>
<svg class="wave" style="top:2924px" viewBox="0 0 60 8"><path d="M0 4 q4 -4 8 0 t8 0 t8 0 t8 0 t8 0 t8 0 t8 0" fill="none" stroke="#1c5fb4" stroke-width="1.6"/></svg>
<div class="step" style="left:176px;top:2959px">
  <svg width="48" height="30" viewBox="0 0 48 30"><path d="M4 20h30l8-6-4-2-8 4H12L6 8H2l4 12z M14 26h28" fill="none" stroke="#2f7ac8" stroke-width="2" stroke-linejoin="round"/></svg>Arrive</div>
<div class="step" style="left:356px;top:2979px">
  <svg width="40" height="40" viewBox="0 0 40 40"><circle cx="20" cy="20" r="16" fill="none" stroke="#2f7ac8" stroke-width="2" stroke-dasharray="80 20"/><path d="M12 20l6 6 12-13" fill="none" stroke="#2f7ac8" stroke-width="2.4"/></svg>Check-In</div>
<div class="step" style="left:528px;top:2959px">
  <svg width="34" height="38" viewBox="0 0 34 38"><path d="M17 2L3 8v10c0 9 6 15 14 18 8-3 14-9 14-18V8z" fill="none" stroke="#2f7ac8" stroke-width="2"/><path d="M10 19l5 5 9-10" fill="none" stroke="#2f7ac8" stroke-width="2"/></svg>Safety<br>Briefing</div>
<div class="step" style="left:693px;top:2979px">
  <svg width="48" height="30" viewBox="0 0 48 30"><path d="M4 18h28l10-7-3-2-9 5H14L8 6H4l4 12z M8 26h36" fill="none" stroke="#2f7ac8" stroke-width="2" stroke-linejoin="round"/></svg>Flight</div>
<div class="step last" style="left:865px;top:2959px">
  <svg width="42" height="36" viewBox="0 0 42 36"><rect x="2" y="6" width="32" height="26" rx="3" fill="none" stroke="#2f7ac8" stroke-width="2"/><path d="M8 2h32v26" fill="none" stroke="#2f7ac8" stroke-width="2"/><path d="M6 28l9-10 7 7 5-5 7 8" fill="none" stroke="#2f7ac8" stroke-width="2"/><circle cx="25" cy="14" r="3" fill="none" stroke="#2f7ac8" stroke-width="2"/></svg>Photos</div>

<!-- FAQ -->
<section>
  <div class="mark" style="left:355px;top:3285px;font-size:56px">SR</div>
  <div class="mark" style="left:970px;top:3405px;font-size:130px">SR</div>
  <h2 class="h2" style="top:3280px">Frequently<span>Asked Questions</span></h2>
  <svg class="wave" style="top:3355px" viewBox="0 0 60 8"><path d="M0 4 q4 -4 8 0 t8 0 t8 0 t8 0 t8 0 t8 0 t8 0" fill="none" stroke="#1c5fb4" stroke-width="1.6"/></svg>
  <div class="faq" style="top:3392px;height:58px"><div class="q open">What Is Lorem Ipsum?<span class="tog on"></span></div><div class="a">Lorem Ipsum Dolor Sit Amet, Consectetur Adipiscing Elit.</div></div>
  <div class="faq" style="top:3462px"><div class="q">Why Do We Use It?<span class="tog"></span></div></div>
  <div class="faq" style="top:3509px"><div class="q">Where Does It Come From?<span class="tog"></span></div></div>
  <div class="faq" style="top:3556px"><div class="q">Where Can I Get Some?<span class="tog"></span></div></div>
  <a class="btn" style="left:558px;top:3622px;width:84px;height:30px;text-transform:none">View All</a>
</section>

<!-- SHORTS -->
<section class="band" style="top:3734px;height:552px"></section>
<div class="mark" style="left:730px;top:3800px;font-size:56px;color:#d5e3f4">SR</div>
<h2 class="h2" style="top:3804px">Shorts Video</h2>
<svg class="wave" style="top:3850px" viewBox="0 0 60 8"><path d="M0 4 q4 -4 8 0 t8 0 t8 0 t8 0 t8 0 t8 0 t8 0" fill="none" stroke="#1c5fb4" stroke-width="1.6"/></svg>
<div class="short" role="img" aria-label="Short clip: thrilling flight over Tampa Bay" style="left:-8px;background:linear-gradient(180deg,#6f8aa5,#9aa3ab 50%,#6b6e73)"><i></i></div>
<div class="short" role="img" aria-label="Short clip: helicopter ride cockpit view" style="left:198px;background:linear-gradient(180deg,#6e7d94,#3a4250 60%,#8a8f97)"><i></i></div>
<div class="short" role="img" aria-label="Short clip: flying around Tampa" style="left:403px;background:linear-gradient(180deg,#9bbfe0,#cfd7df 45%,#3b4048)"><i></i></div>
<div class="short" role="img" aria-label="Short clip: helicopter landing on a pad" style="left:609px;background:linear-gradient(180deg,#b9cde0,#8b9aa8 55%,#3d4550)"><i></i></div>
<div class="short" role="img" aria-label="Short clip: city lights at night from the air" style="left:814px;background:linear-gradient(180deg,#3a3f50,#6a5646 55%,#1d222c)"><i></i></div>
<div class="short" role="img" aria-label="Short clip: coastline at sunset" style="left:1022px;background:linear-gradient(180deg,#c8a49a,#9aa6b5 50%,#4a5766)"><i></i></div>
<a class="social" style="left:429px;background:#5aa8ea"><i></i>skyROAMER</a>
<a class="social" style="left:609px;background:#111"><i></i>skyROAMER</a>

<!-- INQUIRY -->
<section>
  <div class="mark" style="left:380px;top:4370px;font-size:56px">SR</div>
  <h2 class="h2" style="top:4374px">Quick Inquiry</h2>
  <svg class="wave" style="top:4418px" viewBox="0 0 60 8"><path d="M0 4 q4 -4 8 0 t8 0 t8 0 t8 0 t8 0 t8 0 t8 0" fill="none" stroke="#1c5fb4" stroke-width="1.6"/></svg>
  <div class="field" style="left:325px;top:4448px;width:268px">First Name</div>
  <div class="field" style="left:607px;top:4448px;width:268px">Last Name</div>
  <div class="field" style="left:325px;top:4497px;width:268px">Email</div>
  <div class="field" style="left:607px;top:4497px;width:268px">Phone</div>
  <div class="field" style="left:325px;top:4546px;width:550px;height:82px">How Can We Help?</div>
  <a class="btn" style="left:560px;top:4660px;width:78px;height:31px;text-transform:none">Submit</a>
</section>

<div class="weather">
  <div>New York</div>
  <b>49°</b>
  <div style="position:absolute;right:10px;top:10px;width:12px;height:12px;border-radius:50%;background:#f5b830"></div>
  <div style="position:absolute;right:8px;bottom:6px">Clear sky</div>
</div>

<!-- FOOTER -->
<footer class="footer" role="img" aria-label="Faded aerial photo of a helicopter behind the footer"></footer>
<div class="foot-brand"><i></i>SkyROAMER</div>
<div class="foot-h" style="left:382px;top:4832px">Contact Us</div>
<div class="contact" style="top:4860px"><svg width="12" height="12" viewBox="0 0 12 12"><path d="M3 1l2 3-1 1.5c.7 1.4 1.6 2.3 3 3L8.5 7l3 2-1 2C5 11 1 7 1 2z" fill="none" stroke="#fff" stroke-width="1"/></svg><div>(555) SKY-ROAM,<br>(555) 010-4821</div></div>
<div class="contact" style="top:4898px"><svg width="12" height="10" viewBox="0 0 12 10"><rect x=".5" y=".5" width="11" height="9" fill="none" stroke="#fff"/><path d="M.5 .5l5.5 5 5.5-5" fill="none" stroke="#fff"/></svg><div>hello@skyroamer-example.com</div></div>
<div class="contact" style="top:4924px"><svg width="10" height="13" viewBox="0 0 10 13"><path d="M5 12S1 7 1 4.5a4 4 0 018 0C9 7 5 12 5 12z" fill="#fff"/><circle cx="5" cy="4.5" r="1.5" fill="#3a3e45"/></svg><div>12 Harbor Lane<br>Bayview 0000</div></div>
<div class="foot-h" style="left:613px;top:4830px">Quick Links</div>
<ul class="foot-list" style="left:613px;top:4860px"><li>Home</li><li>About Us</li><li>Our Blog</li><li>Careers</li><li>Sarasota</li></ul>
<ul class="foot-list" style="left:691px;top:4860px"><li>Tampa</li><li>Special Events</li><li>Influencer</li><li>Contact Us</li></ul>
<div class="photo" role="img" aria-label="Map showing the Tampa heliport location" style="left:818px;top:4830px;width:225px;height:137px;border-radius:4px;background:linear-gradient(135deg,#eef1f4,#cfe0ee 60%,#a9cde8)">
  <div style="position:absolute;left:64px;top:50px;width:10px;height:10px;border-radius:50%;background:#e23a2c"></div>
</div>
<div class="copy">© 2025 Sky Roamer. All Right Reserved</div>
<div class="sq" style="left:980px"></div>
<div class="sq" style="left:1000px"></div>
<div class="sq" style="left:1024px;border-radius:50%"></div>

</div>
</body>
</html>
```